New Brochure for existing Virtual Reality Amusement Arena

I need a two sided half page brochure for my arcade. it needs to say what we do and what we have to offer. It basically needs to be a paper copy of all the information thats on my website www.kavimo-nix.com
Please check that as it is very informative!
Industry/Entity Type
Entertainment
Colors
Designer to choose colors to be used in the design.
Requirements
Must have
- Color. I have uploaded an old brochure I had made, but now we have a new company and new logo, please make it similar to that. Please pull all pics from my website www.kavimo-nix.com
Should not have
- useless information

```html
<!DOCTYPE html>
<html lang="en">
<head>
<meta charset="utf-8">
<title>Kavimo-Nix Brochure Cover</title>
<link rel="stylesheet" href="https://fonts.googleapis.com/css2?family=Orbitron:wght@600&family=Open+Sans:wght@400;700&display=swap">
<style>
  :root {
    --backdrop: #e6e6e6;
    --ink-light: #ffffff;
    --violet-deep: #3c2f66;
    --violet: #6a4a8c;
    --mauve: #94597e;
    --amber-glow: #a8744f;
    --night-blue: #2a3f8f;
    --web-blue: #3b8fd3;
  }
  * { box-sizing: border-box; margin: 0; padding: 0; }
  html, body {
    width: 1200px;
    height: 790px;
    overflow: hidden;
    background: var(--backdrop);
  }
  .cover {
    position: absolute;
    left: 345px;
    top: 35px;
    width: 510px;
    height: 720px;
    overflow: hidden;
    box-shadow: 0 6px 22px rgba(0,0,0,0.22);
  }
  .cover__photo {
    position: absolute;
    inset: 0;
    background:
      radial-gradient(ellipse at 45% 70%, rgba(168,116,79,0.45), transparent 55%),
      linear-gradient(170deg, var(--violet-deep) 0%, var(--violet) 40%, var(--mauve) 65%, var(--violet-deep) 100%);
  }
  .cover__facets {
    position: absolute;
    inset: 0;
    width: 100%;
    height: 100%;
  }
  .brand {
    position: absolute;
    left: 34px;
    top: 38px;
    display: flex;
    align-items: center;
    gap: 12px;
  }
  .brand__dot {
    width: 30px;
    height: 30px;
    border-radius: 50%;
    background: var(--ink-light);
  }
  .brand__name {
    font-family: "Orbitron", sans-serif;
    font-weight: 600;
    font-size: 27px;
    letter-spacing: 1px;
    color: var(--ink-light);
  }
  .web-band {
    position: absolute;
    right: 0;
    top: 588px;
    width: 215px;
    height: 30px;
    background: var(--web-blue);
    display: flex;
    align-items: center;
    justify-content: center;
    font-family: "Open Sans", sans-serif;
    font-size: 14px;
    color: var(--ink-light);
  }
  .web-band strong { font-weight: 700; }
  .headline {
    position: absolute;
    left: 34px;
    bottom: 38px;
    font-family: "Orbitron", sans-serif;
    font-weight: 600;
    font-size: 25px;
    line-height: 1.08;
    letter-spacing: 1.5px;
    color: var(--ink-light);
    text-transform: uppercase;
  }
</style>
</head>
<body>
  <section class="cover">
    <div class="cover__photo" role="img" aria-label="Photo of a virtual reality motion simulator rig in a dim arena lit in purple and amber"></div>

    <svg class="cover__facets" viewBox="0 0 510 720" preserveAspectRatio="none" aria-hidden="true">
      <polygon points="230,0 420,0 130,720 0,720 0,560" fill="#ffffff" fill-opacity="0.10"/>
      <polygon points="0,0 230,0 0,560" fill="#2a1f4e" fill-opacity="0.18"/>
      <polygon points="330,0 510,0 510,300 430,720 260,720" fill="#1d1a45" fill-opacity="0.16"/>
      <polygon points="510,300 510,720 330,720" fill="#2a3f8f" fill-opacity="0.75"/>
      <polygon points="0,560 0,720 130,720" fill="#241a45" fill-opacity="0.35"/>
    </svg>

    <div class="brand">
      <span class="brand__dot"></span>
      <span class="brand__name">KAVIMO-NIX</span>
    </div>

    <div class="web-band">www.<strong>kavimo-nix</strong>.com</div>

    <h1 class="headline">Gaming like<br>you've never seen</h1>
  </section>
</body>
</html>
```